Horse related business entrepreneur needs a business card

I need a business card design for my horse related business. The enterprise is Tall Fern LLC and I have 3 businesses (headquartered at 2 locations): 1. property management where we rent horse stalls and apartments at a thoroughbred training center outside Ocala; 2. a medium sized transportation service in central Florida that sells horse bedding and removes used horse bedding from horse farms; and horse racing

```html
<!DOCTYPE html>
<html lang="en">
<head>
<meta charset="utf-8">
<title>Tall Fern Farm – Business Card</title>
<link href="https://fonts.googleapis.com/css2?family=Crimson+Pro:ital,wght@0,500;1,500&family=Roboto:wght@400&display=swap" rel="stylesheet">
<style>
  :root {
    --teal: #12698a;
    --orange: #e9794a;
    --ink: #4a4a4a;
    --muted: #8a8a8a;
    --paper: #ffffff;
    --backdrop: #e4e4e2;
  }
  * { box-sizing: border-box; margin: 0; padding: 0; }
  html, body { width: 1200px; height: 960px; overflow: hidden; }
  body { background: var(--backdrop); position: relative; font-family: "Roboto", Arial, sans-serif; }

  .card {
    position: absolute; left: 250px; width: 700px; height: 400px;
    background: var(--paper); overflow: hidden;
    box-shadow: 0 6px 18px rgba(0,0,0,.18);
  }
  .card--front { top: 50px; }
  .card--back { top: 510px; }

  /* Front */
  .brand { position: absolute; top: 120px; left: 0; right: 0; text-align: center; }
  .brand__rule { width: 280px; height: 2px; background: var(--orange); margin: 0 auto 14px; }
  .brand__name {
    font-family: "Crimson Pro", Georgia, serif; font-weight: 500;
    font-size: 46px; letter-spacing: 3px; text-transform: uppercase; color: var(--teal);
  }
  .brand__place {
    font-family: "Crimson Pro", Georgia, serif; font-style: italic; font-weight: 500;
    font-size: 26px; color: var(--orange); margin-top: -4px;
  }
  .addresses {
    position: absolute; top: 292px; left: 0; right: 0; text-align: center;
    font-size: 17px; line-height: 25px; color: var(--ink);
  }

  /* Back */
  .band { position: absolute; top: 0; left: 0; right: 0; height: 212px; background: var(--teal); }
  .band__rule { position: absolute; top: 212px; left: 0; right: 0; height: 6px; background: var(--orange); }
  .band__name {
    position: absolute; top: 58px; left: 0; width: 700px; text-align: center;
    font-family: "Crimson Pro", Georgia, serif; font-weight: 500;
    font-size: 50px; letter-spacing: 3px; text-transform: uppercase; color: var(--paper);
  }
  .band__place {
    position: absolute; top: 120px; left: 0; width: 700px; text-align: center;
    font-family: "Crimson Pro", Georgia, serif; font-style: italic; font-weight: 500;
    font-size: 32px; color: var(--paper);
  }
  .ribbon { position: absolute; top: 178px; left: 160px; width: 380px; height: 58px; }
  .ribbon__text {
    position: absolute; top: 188px; left: 160px; width: 380px; text-align: center;
    font-size: 17px; color: var(--paper); white-space: nowrap;
  }

  .holder { position: absolute; top: 300px; left: 60px; width: 300px; text-align: right; }
  .holder__name {
    font-family: "Crimson Pro", Georgia, serif; font-weight: 500;
    font-size: 34px; letter-spacing: 1px; font-variant: small-caps; color: var(--teal);
  }
  .holder__role {
    font-family: "Crimson Pro", Georgia, serif; font-weight: 500;
    font-size: 17px; letter-spacing: 1px; color: var(--orange); margin-top: -6px;
  }
  .divider { position: absolute; top: 250px; left: 388px; width: 1px; height: 120px; background: #c9c9c9; }

  .contacts { position: absolute; top: 248px; left: 408px; list-style: none; }
  .contacts__item { display: flex; align-items: center; height: 30px; font-size: 16px; color: var(--muted); }
  .contacts__icon { width: 22px; height: 22px; margin-right: 12px; flex: none; }
</style>
</head>
<body>

<section class="card card--front" aria-label="Card front">
  <div class="brand">
    <div class="brand__rule"></div>
    <div class="brand__name">Tall Fern Farm</div>
    <div class="brand__place">Pine Hollow FL</div>
  </div>
  <p class="addresses">
    1520 SE 92nd Lane, Pine Hollow, FL 30001<br>
    780 Willow Ridge Road, Maple Crest, VA 20001
  </p>
</section>

<section class="card card--back" aria-label="Card back">
  <div class="band"></div>
  <div class="band__rule"></div>
  <div class="band__name">Tall Fern Farm</div>
  <div class="band__place">Pine Hollow FL</div>

  <svg class="ribbon" viewBox="0 0 380 58" aria-hidden="true">
    <polygon points="0,0 380,0 362,40 330,58 50,58 18,40" fill="#e9794a"/>
  </svg>
  <div class="ribbon__text">Tall Fern LLC (a family of horse trades)</div>

  <div class="holder">
    <div class="holder__name">Dana Corwell</div>
    <div class="holder__role">OWNER</div>
  </div>
  <div class="divider"></div>

  <ul class="contacts">
    <li class="contacts__item">
      <svg class="contacts__icon" viewBox="0 0 22 22" aria-hidden="true">
        <circle cx="11" cy="11" r="11" fill="#12698a"/>
        <path d="M7.5 6c.6-.4 1.2-.3 1.5.2l1 1.7c.3.5.1 1-.3 1.3l-.6.4c.5 1.2 1.3 2.1 2.4 2.7l.5-.6c.4-.4.9-.5 1.3-.2l1.7 1c.5.3.6.9.2 1.5-.9 1.2-2.3 1.2-3.8.3-1.8-1.1-3.2-2.7-4-4.6-.6-1.5-.6-2.9.1-3.7z" fill="#fff"/>
      </svg>(555) 010-4187
    </li>
    <li class="contacts__item">
      <svg class="contacts__icon" viewBox="0 0 22 22" aria-hidden="true">
        <circle cx="11" cy="11" r="11" fill="#12698a"/>
        <rect x="7.5" y="5.5" width="7" height="4" fill="#fff"/>
        <rect x="5.5" y="9.5" width="11" height="5" rx="1" fill="#fff"/>
        <rect x="7.5" y="13" width="7" height="3.5" fill="#fff" stroke="#12698a" stroke-width=".8"/>
      </svg>(555) 010-2942
    </li>
    <li class="contacts__item">
      <svg class="contacts__icon" viewBox="0 0 22 22" aria-hidden="true">
        <circle cx="11" cy="11" r="11" fill="#12698a"/>
        <rect x="5.5" y="7" width="11" height="8" fill="#fff"/>
        <path d="M5.5 7l5.5 4.5L16.5 7" fill="none" stroke="#12698a" stroke-width="1"/>
      </svg>dana@tallfern.com
    </li>
    <li class="contacts__item">
      <svg class="contacts__icon" viewBox="0 0 22 22" aria-hidden="true">
        <circle cx="11" cy="11" r="11" fill="#12698a"/>
        <circle cx="11" cy="11" r="5.5" fill="none" stroke="#fff" stroke-width="1.2"/>
        <ellipse cx="11" cy="11" rx="2.4" ry="5.5" fill="none" stroke="#fff" stroke-width="1"/>
        <line x1="5.5" y1="11" x2="16.5" y2="11" stroke="#fff" stroke-width="1"/>
      </svg>www.tallfern.com
    </li>
  </ul>
</section>

</body>
</html>
```